Canadian Integrative health and wellness clinic needs a brochure

We need a tri-fold or bi-fold brochure to give out at marketing events and to prospective patients. We would like it to highlight our services offered and our philosophy of care. Please do not include staff profiles as these can change. We would like to give the impression of a cutting edge clinic, with the latest technologies and a patient centred approach.
Updates

Project Deadline Extended
Reason: There have been some excellent designs submitted so far. We have received notice from a few designers that they would like to submit more options in the next few days.

Target Market(s)

We are a clinic that works with families, athletes, seniors and anyone in between.

Industry/Entity Type

Health And Wellness

Font styles to use
Serif

Requirements
Must have
• Logo, info about our services offered, our philosophy of comprehensive treatments and patient centred care, location/contact info.
• I have high resolution images of any image found on our website if you wish to include any of those. www.brivonacare.ca
Nice to have
• colour scheme that includes blues and greys
• something that looks technologically advanced but year still clean and professional
Should not have
• individual staff names or bio's.

```html
<!DOCTYPE html>
<html lang="en">
<head>
<meta charset="utf-8">
<title>Brivona Care – Brochure Cover</title>
<link rel="stylesheet" href="https://fonts.googleapis.com/css2?family=Questrial&family=Arimo:ital,wght@0,400;0,700;1,400;1,700&display=swap">
<style>
  :root {
    --blue: #1e66c8;
    --blue-deep: #1553a8;
    --blue-soft: #dbe7f6;
    --grey-dark: #55585c;
    --grey-mid: #9a9ea3;
    --grey-light: #e9e8e5;
    --paper: #f3f2ef;
    --ink: #26282b;
    --white: #ffffff;
    --stage: #ffffff;
  }
  * { box-sizing: border-box; margin: 0; padding: 0; }
  html, body { width: 1200px; height: 1200px; overflow: hidden; background: var(--stage); }
  .canvas { position: relative; width: 1200px; height: 1200px; }
  .spread {
    position: absolute; left: 100px; top: 250px;
    width: 1000px; height: 700px; display: flex;
    box-shadow: 0 18px 40px rgba(0,0,0,0.12);
  }
  .panel { position: relative; width: 500px; height: 700px; overflow: hidden; }
  .panel svg { position: absolute; inset: 0; }

  .brand {
    position: absolute; display: flex; align-items: center; gap: 10px;
    font-family: "Questrial", sans-serif; font-size: 32px; color: var(--blue-deep);
    letter-spacing: 0.5px; white-space: nowrap;
  }
  .brand-dot { width: 20px; height: 20px; border-radius: 50%; background: var(--blue-deep); }
  .back .brand { left: 0; right: 0; top: 128px; justify-content: center; }
  .front .brand { left: 0; right: 0; top: 42px; justify-content: center; }

  .contact {
    position: absolute; left: 0; right: 0; top: 478px; text-align: center;
    color: var(--white); font-family: "Arimo", sans-serif; font-style: italic;
  }
  .contact-call { font-size: 28px; font-weight: 700; margin-bottom: 14px; white-space: nowrap; }
  .contact-line { font-size: 14px; line-height: 19px; white-space: nowrap; }
  .contact-web {
    margin-top: 20px; font-size: 14px; font-weight: 700; letter-spacing: 5px; font-style: italic;
  }

  .headline {
    position: absolute; left: 89px; top: 470px;
    font-family: "Questrial", sans-serif; text-transform: uppercase; white-space: nowrap;
  }
  .headline-lead { font-size: 45px; color: var(--ink); letter-spacing: -0.5px; line-height: 1; }
  .headline-main { font-size: 74px; color: var(--blue); letter-spacing: -3px; line-height: 0.95; margin-top: 2px; }
  .headline-side {
    position: absolute; left: 384px; top: 586px;
    transform: rotate(-90deg); transform-origin: left top;
    font-family: "Questrial", sans-serif; font-size: 19px; line-height: 22px;
    color: var(--ink); letter-spacing: 1px; white-space: nowrap;
  }
  .front-web {
    position: absolute; left: 0; right: 0; top: 642px; text-align: center;
    font-family: "Arimo", sans-serif; font-weight: 700; font-size: 14px;
    letter-spacing: 5px; color: var(--white);
  }
</style>
</head>
<body>
<div class="canvas">
  <div class="spread">

    <section class="panel back">
      <svg width="500" height="700" viewBox="0 0 500 700">
        <defs>
          <linearGradient id="backPaper" x1="0" y1="0" x2="0" y2="1">
            <stop offset="0" stop-color="#ffffff"/>
            <stop offset="1" stop-color="#e6e6e6"/>
          </linearGradient>
          <linearGradient id="backBlue" x1="0" y1="0" x2="1" y2="1">
            <stop offset="0" stop-color="#2a74d6"/>
            <stop offset="1" stop-color="#1b5fc0"/>
          </linearGradient>
          <linearGradient id="peopleBase" x1="0" y1="0" x2="1" y2="1">
            <stop offset="0" stop-color="#f4f6f8"/>
            <stop offset="0.35" stop-color="#d7c3b2"/>
            <stop offset="0.6" stop-color="#b8bcc1"/>
            <stop offset="1" stop-color="#eef0f2"/>
          </linearGradient>
          <radialGradient id="peopleGlow" cx="0.3" cy="0.45" r="0.6">
            <stop offset="0" stop-color="#8c8f94" stop-opacity="0.55"/>
            <stop offset="1" stop-color="#8c8f94" stop-opacity="0"/>
          </radialGradient>
          <radialGradient id="spineBase" cx="0.5" cy="0.45" r="0.65">
            <stop offset="0" stop-color="#f1f3f5"/>
            <stop offset="0.55" stop-color="#d5dde6"/>
            <stop offset="1" stop-color="#ffffff"/>
          </radialGradient>
        </defs>
        <rect width="500" height="700" fill="url(#backPaper)"/>
        <path d="M0 60 C40 260 200 390 500 410 L500 440 C220 430 40 320 0 160 Z" fill="#d8d8d8" opacity="0.6"/>
        <path d="M0 100 C50 300 220 430 500 440 L500 700 L0 700 Z" fill="url(#backBlue)"/>
        <g class="photo-people" role="img" aria-label="Photo: practitioner showing a spine model to a patient">
          <circle cx="130" cy="320" r="108" fill="#e8eef7"/>
          <circle cx="130" cy="320" r="98" fill="var(--blue-deep)"/>
          <circle cx="130" cy="320" r="92" fill="url(#peopleBase)"/>
          <circle cx="130" cy="320" r="92" fill="url(#peopleGlow)"/>
        </g>
        <g class="photo-spine" role="img" aria-label="Photo: anatomical spine model">
          <circle cx="330" cy="380" r="96" fill="#e8eef7"/>
          <circle cx="330" cy="380" r="86" fill="var(--blue-deep)"/>
          <circle cx="330" cy="380" r="80" fill="url(#spineBase)"/>
        </g>
      </svg>
      <div class="brand"><span class="brand-dot"></span>Brivona Care</div>
      <div class="contact">
        <p class="contact-call">CALL: (403) 555-0147</p>
        <p class="contact-line">Email: info@brivonacare.ca</p>
        <p class="contact-line">1480 Larchmont Avenue NW, Suite 310</p>
        <p class="contact-line">Calgary, Alberta T3P 0K4</p>
        <p class="contact-web">www.brivonacare.ca</p>
      </div>
    </section>

    <section class="panel front">
      <svg width="500" height="700" viewBox="0 0 500 700">
        <defs>
          <linearGradient id="frontPhoto" x1="0" y1="0" x2="1" y2="0">
            <stop offset="0" stop-color="#eef3f6"/>
            <stop offset="0.25" stop-color="#f3ede2"/>
            <stop offset="0.55" stop-color="#f8f8f8"/>
            <stop offset="0.8" stop-color="#c9cdd2"/>
            <stop offset="1" stop-color="#8f959c"/>
          </linearGradient>
          <radialGradient id="frontWarm" cx="0.3" cy="0.5" r="0.35">
            <stop offset="0" stop-color="#e9d2b4" stop-opacity="0.7"/>
            <stop offset="1" stop-color="#e9d2b4" stop-opacity="0"/>
          </radialGradient>
          <radialGradient id="frontCool" cx="0.62" cy="0.55" r="0.3">
            <stop offset="0" stop-color="#b9cde6" stop-opacity="0.6"/>
            <stop offset="1" stop-color="#b9cde6" stop-opacity="0"/>
          </radialGradient>
        </defs>
        <rect width="500" height="700" fill="var(--paper)"/>
        <path d="M0 70 C140 110 320 120 500 110 L500 132 C320 140 140 132 0 100 Z" fill="var(--blue)"/>
        <path d="M0 100 C140 132 320 140 500 132 L500 150 C320 158 140 150 0 118 Z" fill="var(--grey-dark)"/>
        <g class="photo-consult" role="img" aria-label="Photo: clinician explaining a spine model to a patient">
          <path d="M0 118 C140 150 320 158 500 150 L500 410 C340 372 160 372 0 380 Z" fill="url(#frontPhoto)"/>
          <path d="M0 118 C140 150 320 158 500 150 L500 410 C340 372 160 372 0 380 Z" fill="url(#frontWarm)"/>
          <path d="M0 118 C140 150 320 158 500 150 L500 410 C340 372 160 372 0 380 Z" fill="url(#frontCool)"/>
        </g>
        <path d="M0 380 C160 372 340 372 500 410 L500 428 C340 392 160 392 0 400 Z" fill="var(--grey-dark)"/>
        <path d="M230 376 C340 378 430 392 500 410 L500 432 C430 410 340 392 230 376 Z" fill="var(--blue)"/>
        <path d="M0 400 C160 392 340 392 500 432 L500 700 L0 700 Z" fill="var(--grey-light)"/>
        <path d="M0 620 C160 612 340 612 500 620 L500 680 C340 676 160 676 0 680 Z" fill="var(--grey-dark)"/>
      </svg>
      <div class="brand"><span class="brand-dot"></span>Brivona Care</div>
      <div class="headline">
        <p class="headline-lead">Helping You</p>
        <p class="headline-main">Live Life</p>
      </div>
      <p class="headline-side">PAIN FREE</p>
      <p class="front-web">www.brivonacare.ca</p>
    </section>

  </div>
</div>
</body>
</html>
```